TriFold design for a new healthcare company

Looking for a modern design based off some of our older in clinic designs. This is for a start up in which physicians, podiatrists, visit patients in the home called HearthMedix. Logo and wording attached with some stock photos for guidance but not required. Also open to redesigning the logo. QR code also uploaded to be incorporated.

Industry/Entity Type

Healthcare

Colors
0054AA
0677BA
7BADD7
CADEEF
E8F1F8
0094D4
00A9DD
6FCCEA
C7EBF8
E9F6FB

```html
<!DOCTYPE html>
<html lang="en">
<head>
<meta charset="utf-8">
<title>HearthMedix – In-Home Podiatry Trifold</title>
<link href="https://fonts.googleapis.com/css2?family=Montserrat:wght@300;500;600;700;800;900&display=swap" rel="stylesheet">
<style>
  :root {
    --navy: #3e66b3;
    --panel-blue: #4a74bc;
    --sky: #5fa8da;
    --ice: #9ed9ee;
    --ink: #111827;
    --white: #ffffff;
  }
  * { box-sizing: border-box; margin: 0; padding: 0; }
  html, body { width: 1200px; height: 927px; overflow: hidden; background: var(--white); }
  body { font-family: "Montserrat", sans-serif; color: var(--ink); }
  .sheet { position: relative; width: 1200px; height: 927px; overflow: hidden; background: var(--white); }

  .panel-middle { position: absolute; left: 400px; top: 0; width: 400px; height: 927px; background: var(--panel-blue); }
  .art { position: absolute; left: 0; top: 0; }

  .why-title { position: absolute; left: 50px; top: 290px; font-size: 33px; line-height: 33px; font-weight: 900; color: var(--navy); letter-spacing: -0.3px; }
  .bubble-text { position: absolute; text-align: center; font-weight: 800; color: var(--white); white-space: nowrap; }
  .bubble-one { left: 52px; top: 409px; width: 180px; font-size: 20.5px; line-height: 24.5px; }
  .bubble-two { left: 225px; top: 424px; width: 160px; font-size: 18px; line-height: 21.6px; }
  .bubble-three { left: 40px; top: 540px; width: 202px; font-size: 20.5px; line-height: 25px; }
  .here-title { position: absolute; left: 47px; top: 748px; font-size: 43px; line-height: 43px; font-weight: 900; color: var(--ice); letter-spacing: -0.5px; }
  .here-copy { position: absolute; left: 50px; top: 845px; width: 340px; font-size: 14.5px; line-height: 21px; font-weight: 500; white-space: nowrap; }

  .mid-title { position: absolute; left: 430px; top: 289px; font-size: 22.5px; line-height: 26px; font-weight: 700; color: var(--white); }
  .reasons { position: absolute; left: 430px; top: 350px; width: 360px; list-style: none; color: var(--white); font-size: 15px; line-height: 21.2px; font-weight: 500; white-space: nowrap; }
  .reasons li { position: relative; padding-left: 22px; margin-bottom: 8.5px; }
  .reasons li::before { content: ""; position: absolute; left: 1px; top: 7px; width: 6px; height: 6px; border-radius: 50%; background: var(--ice); }
  .solutions-title { position: absolute; left: 429px; top: 562px; font-size: 17px; font-weight: 700; color: var(--white); }
  .solutions { position: absolute; left: 429px; top: 591px; list-style: none; color: var(--white); font-size: 15px; line-height: 21.3px; font-weight: 500; white-space: nowrap; }
  .solutions li { display: flex; align-items: center; gap: 9px; }
  .solutions svg { flex: none; }

  .expect-title { position: absolute; left: 836px; top: 252px; font-size: 21.5px; line-height: 28px; font-weight: 700; color: var(--navy); }
  .step { position: absolute; left: 830px; width: 365px; }
  .step-name { position: absolute; left: 67px; top: 0; font-size: 17px; line-height: 21.5px; font-weight: 700; color: var(--navy); }
  .step-copy { position: absolute; left: 67px; top: 22px; width: 300px; font-size: 15px; line-height: 21.3px; font-weight: 500; white-space: nowrap; }

  .phone { position: absolute; left: 636px; top: 848px; font-size: 50px; font-weight: 300; color: var(--white); letter-spacing: 0.5px; }
</style>
</head>
<body>
<main class="sheet">
  <div class="panel-middle"></div>

  <svg class="art" width="1200" height="927" viewBox="0 0 1200 927">
    <defs>
      <linearGradient id="careGrad" x1="0" y1="0" x2="1" y2="1">
        <stop offset="0" stop-color="#d7dde4"/><stop offset="0.5" stop-color="#9fc3dc"/><stop offset="1" stop-color="#6c8fae"/>
      </linearGradient>
      <linearGradient id="visitGrad" x1="0" y1="0" x2="1" y2="0">
        <stop offset="0" stop-color="#c8ccd0"/><stop offset="0.5" stop-color="#8aa6c0"/><stop offset="1" stop-color="#a7c3dc"/>
      </linearGradient>
      <linearGradient id="teamGrad" x1="0" y1="0" x2="0" y2="1">
        <stop offset="0" stop-color="#4a74bc" stop-opacity="0"/><stop offset="0.35" stop-color="#39498a"/><stop offset="1" stop-color="#27336a"/>
      </linearGradient>
      <linearGradient id="ornamentGrad" x1="0" y1="0" x2="0" y2="1">
        <stop offset="0" stop-color="#5fa8da"/><stop offset="1" stop-color="#4a74bc"/>
      </linearGradient>
    </defs>

    <!-- decorative ornament area -->
    <rect role="img" aria-label="Decorative light-blue footprint-style ornament" x="400" y="0" width="400" height="300" fill="url(#ornamentGrad)"/>

    <!-- photos -->
    <path role="img" aria-label="Photo: podiatrist trimming a patient's toenails" d="M0 0 H467 C455 120 400 228 300 252 C200 275 60 252 0 203 Z" fill="url(#careGrad)"/>
    <rect role="img" aria-label="Photo: podiatrist chatting with a senior patient at home" x="800" y="0" width="400" height="250" fill="url(#visitGrad)"/>
    <rect role="img" aria-label="Photo: the HearthMedix podiatry team in scrubs" x="400" y="690" width="800" height="237" fill="url(#teamGrad)"/>

    <!-- speech bubbles -->
    <circle cx="305" cy="494" r="103" fill="var(--panel-blue)"/>
    <circle cx="142" cy="455" r="88" fill="var(--sky)"/>
    <path d="M140 503 A113 113 0 1 0 230 685 L268 731 L240 676 A113 113 0 0 0 140 503 Z" fill="var(--ice)"/>

    <!-- step icons -->
    <g fill="var(--panel-blue)" stroke="#2e3f6f" stroke-width="1">
      <circle cx="855" cy="346" r="24"/><circle cx="855" cy="418" r="24"/>
      <circle cx="855" cy="503" r="24"/><circle cx="855" cy="606" r="24"/>
    </g>
    <g fill="none" stroke="#fff" stroke-width="1.8" stroke-linecap="round">
      <path d="M866 340 A12 12 0 1 0 867 352"/><path d="M866 335 V341 H860"/><path d="M855 340 V347 H861"/>
      <circle cx="861" cy="412" r="7"/><path d="M856 417 L848 425"/><path d="M843 424 h9 v6 h-9 z"/>
      <rect x="846" y="492" width="16" height="22" rx="2"/><path d="M850 500 h8 M850 505 h8 M850 510 h6"/>
      <path d="M849 616 C846 606 848 598 854 596 C860 596 862 604 860 616"/><path d="M842 600 l-3 -2 M842 606 h-4"/>
    </g>
  </svg>

  <h2 class="why-title">WHY IN-HOME<br>PODIATRY?</h2>
  <p class="bubble-text bubble-one">Difficulty<br>visiting a<br>podiatrist?</p>
  <p class="bubble-text bubble-two">Muscle<br>weakness,<br>walker,<br>wheelchair, or<br>post-surgery<br>restrictions?</p>
  <p class="bubble-text bubble-three">Need<br>specialized<br>foot and ankle<br>care but limited<br>by physical<br>challenges?</p>
  <h2 class="here-title">WE ARE HERE<br>FOR YOU!</h2>
  <p class="here-copy">Offering specialized in-home podiatry<br>services tailored for your unique needs.</p>

  <h2 class="mid-title">Why Patients<br>Opt for In-Home Podiatry</h2>
  <ul class="reasons">
    <li>Challenges in self foot-care due to impaired<br>vision or reduced fine motor skills.</li>
    <li>Muscle weakness or dependency on<br>mobility aids.</li>
    <li>Post-surgery restrictions, arthritis, or other<br>health issues.</li>
    <li>Desire for Medicare-approved foot bath<br>medication delivered to their door.</li>
  </ul>
  <h3 class="solutions-title">Our Solutions</h3>
  <ul class="solutions">
    <li><svg width="13" height="13" viewBox="0 0 13 13"><circle cx="6.5" cy="6.5" r="5.5" fill="none" stroke="#9ed9ee" stroke-width="1.4"/><path d="M4 6.7 L5.9 8.5 L9 4.8" fill="none" stroke="#9ed9ee" stroke-width="1.4"/></svg>Care for a range of foot problems.</li>
    <li><svg width="13" height="13" viewBox="0 0 13 13"><circle cx="6.5" cy="6.5" r="5.5" fill="none" stroke="#9ed9ee" stroke-width="1.4"/><path d="M4 6.7 L5.9 8.5 L9 4.8" fill="none" stroke="#9ed9ee" stroke-width="1.4"/></svg>Relief for in-home caregivers.</li>
    <li><svg width="13" height="13" viewBox="0 0 13 13"><circle cx="6.5" cy="6.5" r="5.5" fill="none" stroke="#9ed9ee" stroke-width="1.4"/><path d="M4 6.7 L5.9 8.5 L9 4.8" fill="none" stroke="#9ed9ee" stroke-width="1.4"/></svg>Expertise in treating older patients.</li>
    <li><svg width="13" height="13" viewBox="0 0 13 13"><circle cx="6.5" cy="6.5" r="5.5" fill="none" stroke="#9ed9ee" stroke-width="1.4"/><path d="M4 6.7 L5.9 8.5 L9 4.8" fill="none" stroke="#9ed9ee" stroke-width="1.4"/></svg>Comprehensive evaluations and treatments.</li>
  </ul>

  <h2 class="expect-title">What to Expect During<br>an In-Home Visit</h2>
  <div class="step" style="top:325px"><h3 class="step-name">Duration</h3><p class="step-copy">Typically 15-25 minutes.</p></div>
  <div class="step" style="top:389px"><h3 class="step-name">Examination</h3><p class="step-copy">Comprehensive check of feet, nails,<br>skin, and potential infections.</p></div>
  <div class="step" style="top:474px"><h3 class="step-name">Evaluation</h3><p class="step-copy">Wound and pressure sore<br>assessment, pulse checks,<br>circulation signs, and nerve tests.</p></div>
  <div class="step" style="top:580px"><h3 class="step-name">Treatment</h3><p class="step-copy">Fungal toenail treatments, callus<br>treatments, injections for arthritis,<br>X-ray imaging (if needed), and more.</p></div>

  <p class="phone">555-214-0386</p>
</main>
</body>
</html>
```